Corvane Power Holdings Website

We have color scheme, logo and content, but need a design options in PDF format for the website. The PDF should guide us in how to use the color scheme and fonts in the site design (what background colors to use where, what link and hover colors to you, when to use which fonts...)

Corvane Power Holdings wants a conservative and straightforward website design that is in line with the banking industry. At the same time, Corvane wants the design to be innovative and cutting-edge in line with the renewable energy industry. Overall, the site design must be present the company as professional, serious, knowledgeable, experienced, reliable, and successful as well as a global good citizen.
Updates

We are closing this project. Thank you all for your beautiful work. Our designer was sick, but informed us today that she is better and able to resume her work. So we are closing this project and restarting work with her. Wish you all health and success.

Target Market(s)

investors, partners, developers, investment community, private equity community

Industry/Entity Type

Investment

Number of Pages Required

2 page

Requirements
Must have
• The color scheme is attached.
The logo is attached.
Fonts are Questrial and Cormorant (as used in logo).
The site must use these colors and fonts and logo design.

The 2 pages we need designed are the homepage and the portfolio page.
Homepage - The portfolio map on the homepage will be an image like with hotspots that link to portfolio items. This map image might go well with logo:
https://www.pictavo-stock.example/abstract-polygon-world-map-vector-illustration-geometric-structure-in-blue-color-for-presentation-booklet-website-and-other-design-projects-pol-image552093418.html
But we would need to zoom in on Israel and EU, and leave out US / Asia-Pacific.
The way the map will work technically (using hotspots) should be something like:
https://brindlepower.example.il/geographic-spread/.
Portfolio Page - The portfolio map there will be a Google Map/
Nice to have
• The content for the site is attached as a Word Doc, and much of it is in place at http://corvanefund.example.host4821.sample-server.example/. The design must fit this content, but we are open to some layout changes.
Design Requests:
• nav bar – light animation like https://pellucovet.example/ and https://www.tq-residencylaw.example/
• innovative, unique design with welcoming, appealing, modern feel
• engaging content display by using parallax and subtle movement
• clean, intuitive, easy to navigation layout

```html
<!DOCTYPE html>
<html lang="en">
<head>
<meta charset="utf-8">
<title>Corvane Power Holdings</title>
<link rel="stylesheet" href="https://fonts.googleapis.com/css2?family=Cormorant+Garamond:wght@600;700&family=Questrial&display=swap">
<style>
  :root {
    --green-deep: #124f3e;
    --green-button: #5ba56b;
    --hero-teal-a: #4f7d74;
    --hero-teal-b: #2f5f58;
    --panel-blue: #1c4f7a;
    --panel-slate: #5f6e7a;
    --map-cyan: #cdebf1;
    --text-body: #222;
    --white: #fff;
    --footer-bg: #1b1b1b;
    --footer-bar: #0e0e0e;
    --link-green: #5ba56b;
  }
  * { box-sizing: border-box; margin: 0; padding: 0; }
  html, body { width: 1200px; height: 2817px; overflow: hidden; background: var(--white); }
  body { position: relative; font-family: "Questrial", sans-serif; color: var(--text-body); }
  .abs { position: absolute; }
  .serif { font-family: "Cormorant Garamond", serif; font-weight: 700; font-variant-numeric: lining-nums; }

  .hero { left: 0; top: 0; width: 1200px; height: 616px;
    background: linear-gradient(170deg, var(--hero-teal-a), var(--hero-teal-b)); }
  .brand { left: 85px; top: 26px; display: flex; align-items: center; gap: 10px; color: var(--white); }
  .brand-dot { width: 52px; height: 52px; border-radius: 50%; background: #c6d93a; }
  .brand-name { font-family: "Cormorant Garamond", serif; font-weight: 700; font-size: 34px; letter-spacing: 1px; line-height: 1; }
  .nav { top: 43px; font-size: 15px; color: var(--white); }
  .nav a { position: absolute; color: var(--white); text-decoration: none; white-space: nowrap; }
  .search { left: 1069px; top: 41px; }
  .hero-title { left: 0; width: 1200px; top: 280px; text-align: center; font-size: 58px; color: var(--white); letter-spacing: 1px; line-height: 1; }
  .hero-sub { left: 0; width: 1200px; top: 356px; text-align: center; font-size: 19px; color: var(--white); }

  .stat { width: 220px; text-align: center; }
  .stat-num { font-family: "Cormorant Garamond", serif; font-weight: 700; font-size: 50px; color: var(--green-deep); line-height: 1; font-variant-numeric: lining-nums; }
  .stat-label { margin-top: 14px; font-size: 14.5px; }

  .split { left: 90px; top: 839px; width: 993px; height: 357px; }
  .panel-copy { color: var(--white); }
  .panel-copy h2 { font-family: "Cormorant Garamond", serif; font-weight: 700; font-size: 29px; line-height: 36px; letter-spacing: 1px; }
  .panel-copy p { font-size: 14px; line-height: 25.5px; margin-top: 24px; }
  .btn { display: inline-block; width: 148px; height: 40px; line-height: 40px; border-radius: 20px; text-align: center;
    background: var(--green-button); color: var(--white); font-size: 13px; text-decoration: none; }

  .strategy-title { left: 0; width: 1200px; top: 1278px; text-align: center; font-size: 47px; color: var(--green-deep); letter-spacing: 1.5px; line-height: 1; }
  .strategy-body { left: 200px; width: 800px; top: 1354px; text-align: center; font-size: 14.5px; line-height: 25.5px; }

  .band { left: 0; top: 1563px; width: 1200px; height: 298px; background: linear-gradient(180deg, #35474a, #4a5a50); }
  .band-title { left: 89px; top: 1676px; font-size: 60px; color: var(--white); line-height: 1; letter-spacing: 1px; }
  .band-sub { left: 89px; top: 1749px; font-size: 19px; color: var(--white); }

  .portfolio-intro { left: 200px; width: 800px; top: 1936px; text-align: center; font-size: 14.5px; line-height: 25.5px; }
  .map { left: 191px; top: 2035px; width: 785px; height: 470px; border-radius: 40px;
    background: radial-gradient(ellipse at center, var(--map-cyan), #e8f6f9 75%, var(--white)); }

  .footer { left: 0; top: 2565px; width: 1200px; height: 197px; background: var(--footer-bg); color: var(--white); }
  .footer-address { left: 94px; top: 66px; font-size: 14.5px; line-height: 26px; }
  .footer-contacts { left: 94px; top: 130px; display: flex; gap: 30px; font-size: 11.5px; align-items: center; }
  .footer-contacts span { display: flex; align-items: center; gap: 7px; }
  .footer-contacts .mail { color: var(--link-green); }
  .social { left: 964px; top: 85px; display: flex; gap: 11px; }
  .social span { width: 27px; height: 27px; border-radius: 50%; background: var(--white); display: block; }
  .footer-bar { left: 0; top: 2762px; width: 1200px; height: 55px; background: var(--footer-bar); color: var(--white); }
  .bar-brand { left: 93px; top: 17px; font-size: 17px; }
  .bar-copy { left: 0; width: 1200px; top: 19px; text-align: center; font-size: 14px; }
  .to-top { left: 1081px; top: 16px; }
</style>
</head>
<body>

  <section class="hero abs" role="img" aria-label="Aerial photograph of a large solar farm under a teal overlay"></section>
  <div class="brand abs"><span class="brand-dot"></span><span class="brand-name">CORVANE</span></div>
  <nav class="nav abs">
    <a style="left:767px">About</a>
    <a style="left:832px">Strategy</a>
    <a style="left:909px">Portfolio</a>
    <a style="left:982px">Contact</a>
  </nav>
  <svg class="search abs" width="22" height="22" viewBox="0 0 22 22" fill="none" stroke="#fff" stroke-width="1.6">
    <circle cx="9" cy="9" r="7"/><line x1="14" y1="14" x2="20" y2="20"/>
  </svg>
  <h1 class="hero-title abs serif">ILLUMINATING THE FUTURE</h1>
  <p class="hero-sub abs">Investing in clean energy to generate sustainable returnsfor our investors and planet</p>

  <div class="stat abs" style="left:127px;top:692px"><div class="stat-num">10</div><div class="stat-label">Years of Operation</div></div>
  <div class="stat abs" style="left:305px;top:692px"><div class="stat-num">6</div><div class="stat-label">Countries of Investments</div></div>
  <div class="stat abs" style="left:511px;top:692px"><div class="stat-num">600</div><div class="stat-label">MW under Management</div></div>
  <div class="stat abs" style="left:711px;top:692px;width:300px"><div class="stat-num">€500,000,000</div><div class="stat-label">Assets under Management</div></div>

  <svg class="split abs" width="993" height="357" viewBox="0 0 993 357">
    <polygon points="0,0 655,0 541,357 0,357" fill="var(--panel-blue)" role="img" aria-label="Photograph of an industrial power plant under a blue overlay"/>
    <polygon points="666,0 993,0 993,357 552,357" fill="var(--panel-slate)" role="img" aria-label="Photograph of a wind turbine in a field under a slate overlay"/>
  </svg>
  <div class="panel-copy abs" style="left:151px;top:890px;width:460px">
    <h2>EXPERTISE.<br>RESOURCEFULNESS.<br>INTEGRITY.</h2>
    <p>Funding clean energy projects that maximise value to&nbsp; our investors<br>and contribute to a more sustainable world</p>
  </div>
  <a class="btn abs" style="left:151px;top:1120px">ABOUT US</a>
  <div class="panel-copy abs" style="left:789px;top:890px;width:270px">
    <h2>HANDS-ON<br>INVESTMENT<br>MANAGEMENT</h2>
    <p>Utilising our multi-disciplinary<br>knowledge, sector expertise, extensive<br>experience and collaborative spirit</p>
  </div>
  <a class="btn abs" style="left:789px;top:1120px">OUR TEAM</a>

  <h2 class="strategy-title abs serif">PROVEN INVESTMENT STRATEGY</h2>
  <p class="strategy-body abs">Achieving consistently high annualized returns and capital gains by leveragingour energy sector experience, broad geographic footprint, dedicated local networks, value creation and implementation of platform structures</p>
  <a class="btn abs" style="left:526px;top:1437px">OUR APPROACH</a>

  <section class="band abs" role="img" aria-label="Aerial photograph of a wind turbine over an industrial landscape"></section>
  <h2 class="band-title abs serif">ILLUMINATING THE FUTURE</h2>
  <p class="band-sub abs">Investing in clean energy to generate sustainable returnsfor our investors and planet</p>

  <p class="portfolio-intro abs">Corvane’ energy funds provide a diversified portfolio of assets - in operation and under construction, in multiple markets - that<br>drive high investment returns and a balanced risk profile.</p>
  <div class="map abs" role="img" aria-label="Polygon world map with portfolio hotspots in the UK, Poland, Netherlands, Italy, Spain and Israel"></div>

  <footer class="footer abs">
    <div class="footer-address abs">Corvane Power Holdings, Kfar Dalia 6091200 Israel<br>Lumen Building, Orchard Park</div>
    <div class="footer-contacts abs">
      <span class="mail"><svg width="13" height="9" viewBox="0 0 13 9"><rect width="13" height="9" fill="#fff"/><polyline points="0,0 6.5,5 13,0" fill="none" stroke="#1b1b1b" stroke-width="1.2"/></svg>info@corvanefund.example</span>
      <span><svg width="13" height="13" viewBox="0 0 24 24" fill="#fff"><path d="M6.6 10.8c1.4 2.8 3.8 5.1 6.6 6.6l2.2-2.2c.3-.3.7-.4 1-.2 1.1.4 2.3.6 3.6.6.6 0 1 .4 1 1V20c0 .6-.4 1-1 1C10.6 21 3 13.4 3 4c0-.6.4-1 1-1h3.5c.6 0 1 .4 1 1 0 1.3.2 2.5.6 3.6.1.3 0 .7-.2 1z"/></svg>Israel: +972-3-555-0142</span>
      <span><svg width="13" height="13" viewBox="0 0 24 24" fill="#fff"><path d="M6.6 10.8c1.4 2.8 3.8 5.1 6.6 6.6l2.2-2.2c.3-.3.7-.4 1-.2 1.1.4 2.3.6 3.6.6.6 0 1 .4 1 1V20c0 .6-.4 1-1 1C10.6 21 3 13.4 3 4c0-.6.4-1 1-1h3.5c.6 0 1 .4 1 1 0 1.3.2 2.5.6 3.6.1.3 0 .7-.2 1z"/></svg>Europe: +44 (0) 20 7946 0321</span>
    </div>
    <div class="social abs"><span></span><span></span><span></span><span></span></div>
  </footer>
  <div class="footer-bar abs">
    <div class="bar-brand abs">SiteForge</div>
    <div class="bar-copy abs">© 2020 Corvane Power Holdings</div>
    <svg class="to-top abs" width="24" height="24" viewBox="0 0 24 24"><circle cx="12" cy="12" r="12" fill="var(--green-button)"/><path d="M12 7v10M8 11l4-4 4 4" fill="none" stroke="#fff" stroke-width="1.6"/></svg>
  </div>

</body>
</html>
```